New Business Card for General Contractor Marketing

Need a business card the is more like a marketing promotion of our services
Must be horizontal orientation, One Sided Only, Max font size, Organize the Services
#1 General Contractor for Realtors
Remodels – Renovations – Repairs
Water & Mold Damage Experts
Painting: Interior/ Exterior
Flooring: Wood / LVT / Carpet
Plumbing: Repairs & Upgrades
Electric: Lights & Energy Efficient Upgrades
Kitchen & Bath Remodels
Fast Inspections Repair Billed Thru Escrow
BrightHarborBuilds.com
555-418-2796

Industry/Entity Type

General Contractor

Contact Information for Business Card

One Sided Only: #1 General Contractor for Realtors Remodels – Renovations – Repairs Water & Mold Damage Experts Painting: Interior/ Exterior Flooring: Wood / LVT / Carpet Plumbing: Repairs & Upgrades Electric: Lights & Energy Efficient Upgrades Kitchen & Bath Remodels Fast Inspections Repair Billed Thru Escrow BrightHarborBuilds.com 555-418-2796

Colors
0054AA
0677BA
7BADD7
CADEEF
E8F1F8

Requirements
Must have
• One Sided Only: #1 General Contractor for Realtors Remodels – Renovations – Repairs Water & Mold Damage Experts Painting: Interior/ Exterior Flooring: Wood / LVT / Carpet Plumbing: Repairs & Upgrades Electric: Lights & Energy Efficient Upgrades Kitchen & Bath Remodels Fast Inspections Repair Billed Thru Escrow BrightHarborBuilds.com 555-418-2796

```html
<!DOCTYPE html>
<html lang="en">
<head>
<meta charset="utf-8">
<title>Bright Harbor Builds – Business Card</title>
<link rel="stylesheet" href="https://fonts.googleapis.com/css2?family=Michroma&family=Jost:wght@400;700&family=Saira+Extra+Condensed:wght@500&display=swap">
<style>
  :root {
    --blue-deep: #0054AA;
    --blue-mid: #0677BA;
    --blue-band: #1259AF;
    --blue-light: #7BADD7;
    --blue-pale: #CADEEF;
    --blue-mist: #E8F1F8;
    --white: #FFFFFF;
    --stage: #E3E7EC;
    --font-display: "Michroma", "Arial", sans-serif;
    --font-body: "Jost", "Helvetica", sans-serif;
    --font-condensed: "Saira Extra Condensed", "Arial Narrow", sans-serif;
  }
  * { margin: 0; padding: 0; box-sizing: border-box; }
  html, body { width: 1200px; height: 1200px; overflow: hidden; }
  body { background: var(--stage); position: relative; }

  .card {
    position: absolute; left: 50px; top: 285px;
    width: 1100px; height: 630px;
    background: var(--white);
    overflow: hidden;
    box-shadow: 0 10px 30px rgba(0,0,0,.18);
  }
  .card-shapes { position: absolute; inset: 0; }

  .kitchen-photo {
    position: absolute; inset: 0;
    clip-path: polygon(780px 62px, 1100px 62px, 1100px 440px, 470px 440px);
    background: linear-gradient(180deg, #eef0f2 0%, #dcdfe2 38%, #c8c9c8 60%, #9c7d5f 82%, #7a5a3f 100%);
  }

  .site-url {
    position: absolute; left: 34px; top: 14px;
    font-family: var(--font-display); font-size: 28px;
    color: var(--white); letter-spacing: .5px;
  }

  .trade-list {
    position: absolute; left: 30px; top: 70px;
    list-style: none;
    font-family: var(--font-body); font-size: 28px; line-height: 30px;
    color: var(--blue-deep);
  }
  .trade-list strong { font-weight: 700; }

  .specialty-list {
    position: absolute; left: 30px; top: 200px;
    list-style: none;
    font-family: var(--font-body); font-size: 30px; line-height: 42px;
    color: var(--white);
  }

  .call-label {
    position: absolute; left: 34px; top: 345px;
    font-family: var(--font-condensed); font-weight: 500; font-size: 40px;
    color: var(--blue-mid); letter-spacing: 1px;
  }
  .call-number {
    position: absolute; left: 28px; top: 410px;
    font-family: var(--font-display); font-size: 44px;
    color: var(--blue-deep);
  }

  .company-name {
    position: absolute; right: 30px; top: 446px;
    text-align: right;
    font-family: var(--font-display); font-size: 30px; line-height: 36px;
    color: var(--blue-deep);
  }

  .services-strip {
    position: absolute; left: 0; top: 522px; width: 1100px;
    text-align: center; padding-left: 260px;
    font-family: var(--font-display); font-size: 24px;
    color: var(--white);
  }
  .tagline-strip {
    position: absolute; left: 0; top: 582px; width: 1100px;
    text-align: center;
    font-family: var(--font-display); font-size: 28px;
    color: var(--white);
  }
</style>
</head>
<body>
  <section class="card">
    <svg class="card-shapes" viewBox="0 0 1100 630" width="1100" height="630" aria-hidden="true">
      <rect class="header-band" x="0" y="0" width="1100" height="62" fill="var(--blue-band)"/>
      <polygon class="specialty-band" points="0,195 671,195 556,335 0,335" fill="var(--blue-band)"/>
      <polygon class="call-tab" points="380,335 450,335 505,398 440,398" fill="var(--blue-light)"/>
      <polygon class="call-point" points="450,335 556,335 505,398" fill="var(--blue-band)"/>
      <rect class="services-band" x="0" y="518" width="1100" height="48" fill="var(--blue-band)"/>
      <rect class="tagline-band" x="0" y="572" width="1100" height="58" fill="var(--blue-light)"/>
    </svg>

    <div class="kitchen-photo" role="img" aria-label="Photo of a remodeled white kitchen with island, stools, stainless fridge and wood floors"></div>

    <div class="site-url">BrightHarborBuilds.com</div>

    <ul class="trade-list">
      <li><strong>Painting:</strong> Interior/ Exterior</li>
      <li><strong>Flooring:</strong> Wood / LVT / Carpet</li>
      <li><strong>Plumbing:</strong> Repairs &amp; Upgrades</li>
      <li><strong>Electric:</strong> Lights &amp; Energy Efficient Upgrades</li>
    </ul>

    <ul class="specialty-list">
      <li>Water &amp; Mold Damage Experts</li>
      <li>Kitchen &amp; Bath Remodels</li>
      <li>Fast Inspections Repair Billed Thru Escrow</li>
    </ul>

    <div class="call-label">CALL/TEXT</div>
    <div class="call-number">555-418-2796</div>

    <div class="company-name">BRIGHT HARBOR<br>BUILDS INC.</div>

    <div class="services-strip">REMODELS – RENOVATIONS – REPAIRS</div>
    <div class="tagline-strip">#1 GENERAL CONTRACTOR FOR REALTORS</div>
  </section>
</body>
</html>
```